label design for cannabis

label template 4"x5.5" for a Massachusetts cannabis beverage product. labels will be transparent and placed on a blue (pantone 306C) bag.
https://www.drizzlepods.com/

Target Market(s)

cannabis customers in MA, 21+

Industry/Entity Type

cannabis consumer product

Font styles to use
Other font styles liked:
• DIN

Colors
0094D4
00A9DD
6FCCEA
C7EBF8
E9F6FB

Requirements
Must have
• label design with fizz logo, flavor (lemon, lime, plain, and coffee). 306C pantone for background and 11-0601 TCX for text. font=DINackground.
Nice to have
• tray icon, illustrated ice cubes in white (clear), yellow (lemon), green (lime) and brown (coffee)
Should not have
• no cartoonish characters

```html
<!DOCTYPE html>
<html lang="en">
<head>
<meta charset="utf-8">
<title>fizz infused ice cubes — flavour labels</title>
<link rel="stylesheet" href="https://fonts.googleapis.com/css2?family=Barlow+Condensed:wght@500;600;700&family=Barlow+Semi+Condensed:wght@700&display=swap">
<style>
  :root {
    --sheet: #ffffff;
    --bag-blue: #02aeef;
    --label-white: #f6f6f4;
    --lemon: #f2f200;
    --lime: #b4f51f;
    --coffee: #4a2410;
    --classic: #ffffff;
  }
  * { box-sizing: border-box; margin: 0; padding: 0; }
  html, body {
    width: 911px; height: 1200px; overflow: hidden;
    background: var(--sheet);
  }
  .sheet { position: relative; width: 911px; height: 1200px; }

  .label {
    position: absolute;
    width: 385px; height: 530px;
    background: var(--bag-blue);
    color: var(--label-white);
    font-family: "Barlow Condensed", sans-serif;
    --ink: var(--classic);
  }
  .label--lemon   { left: 48px;  top: 53px;  --ink: var(--lemon); }
  .label--lime    { left: 460px; top: 53px;  --ink: var(--lime); }
  .label--coffee  { left: 48px;  top: 603px; --ink: var(--coffee); }
  .label--classic { left: 460px; top: 603px; --ink: var(--classic); width: 382px; height: 525px; }

  .brand {
    position: absolute; left: 0; right: 0; top: 18px;
    text-align: center;
    font-family: "Barlow Semi Condensed", sans-serif;
    font-weight: 700; font-size: 150px; line-height: 1;
    letter-spacing: -2px;
    color: var(--label-white);
  }
  .brand__tm {
    position: absolute; left: 284px; top: 40px;
    font-family: "Barlow Condensed", sans-serif;
    font-size: 10px; font-weight: 500; color: var(--label-white);
  }
  .tagline {
    position: absolute; left: 0; right: 0; top: 146px;
    text-align: center;
    font-weight: 500; font-size: 41px; line-height: 1;
    letter-spacing: 0.3px;
  }

  .cubes-art {
    position: absolute; left: 133px; top: 211px;
    width: 118px; height: 91px;
    border-radius: 8px;
    background: var(--ink);
    opacity: 0.35;
  }

  .tray { position: absolute; left: 110px; top: 329px; width: 171px; height: 50px; }
  .tray__bar {
    position: absolute; left: 0; top: 0; width: 171px; height: 26px;
    border: 2px solid var(--ink);
    color: var(--ink);
    font-weight: 600; font-size: 15px; line-height: 22px;
    text-align: center;
  }
  .tray__wells { position: absolute; left: 0; top: 24px; width: 171px; height: 26px; }

  .flavour {
    position: absolute; left: 0; right: 0; top: 380px;
    text-align: center; color: var(--ink);
    font-weight: 700; font-size: 46px; line-height: 1;
  }
  .dose {
    position: absolute; left: 0; right: 0; top: 424px;
    text-align: center; color: var(--ink);
    font-weight: 600; font-size: 19px; line-height: 1;
  }

  .thc-warning { position: absolute; left: 17px; top: 456px; width: 52px; text-align: center; }
  .thc-warning svg { display: block; margin: 0 auto; }
  .thc-warning__text {
    display: block; margin-top: 2px;
    font-weight: 600; font-size: 10.5px; line-height: 1; white-space: nowrap;
  }

  .kids-warning { position: absolute; left: 315px; top: 456px; width: 50px; height: 48px; }
  .kids-warning svg { position: absolute; inset: 0; }
  .kids-warning__text {
    position: absolute; left: 0; right: 0; top: 13px;
    text-align: center; font-weight: 600; font-size: 11px; line-height: 11px;
  }
</style>
</head>
<body>
<main class="sheet">

  <section class="label label--lemon">
    <h1 class="brand">fizz</h1><span class="brand__tm">TM</span>
    <p class="tagline">infused ice cubes</p>
    <div class="cubes-art" role="img" aria-label="Line illustration of three stacked melting ice cubes in lemon yellow"></div>
    <div class="tray">
      <div class="tray__bar">5mg per cube</div>
      <svg class="tray__wells" viewBox="0 0 171 26" fill="none" stroke="currentColor" stroke-width="2" style="color:var(--ink)">
        <path d="M6 1 L10 25 H29 L32 1 M37 1 L40 25 H59 L62 1 M69 1 L72 25 H91 L94 1 M101 1 L104 25 H123 L126 1 M133 1 L136 25 H156 L160 1"/>
      </svg>
    </div>
    <h2 class="flavour">lemon</h2>
    <p class="dose">50mg per tray</p>
    <div class="thc-warning">
      <svg width="42" height="36" viewBox="0 0 42 36" fill="none" stroke="#fff" stroke-width="2.5" stroke-linejoin="round"><path d="M21 3 L39 33 H3 Z"/></svg>
      <span class="thc-warning__text">CONTAINS THC</span>
    </div>
    <div class="kids-warning">
      <svg viewBox="0 0 50 48" fill="none" stroke="#fff" stroke-width="2.5"><polygon points="15,2 35,2 48,14 48,34 35,46 15,46 2,34 2,14"/><path d="M20 7 H30 M20 41 H30"/></svg>
      <p class="kids-warning__text">NOT SAFE<br>FOR KIDS</p>
    </div>
  </section>

  <section class="label label--lime">
    <h1 class="brand">fizz</h1><span class="brand__tm">TM</span>
    <p class="tagline">infused ice cubes</p>
    <div class="cubes-art" role="img" aria-label="Line illustration of three stacked melting ice cubes in lime green"></div>
    <div class="tray">
      <div class="tray__bar">5mg per cube</div>
      <svg class="tray__wells" viewBox="0 0 171 26" fill="none" stroke="currentColor" stroke-width="2" style="color:var(--ink)">
        <path d="M6 1 L10 25 H29 L32 1 M37 1 L40 25 H59 L62 1 M69 1 L72 25 H91 L94 1 M101 1 L104 25 H123 L126 1 M133 1 L136 25 H156 L160 1"/>
      </svg>
    </div>
    <h2 class="flavour">lime</h2>
    <p class="dose">50mg per tray</p>
    <div class="thc-warning">
      <svg width="42" height="36" viewBox="0 0 42 36" fill="none" stroke="#fff" stroke-width="2.5" stroke-linejoin="round"><path d="M21 3 L39 33 H3 Z"/></svg>
      <span class="thc-warning__text">CONTAINS THC</span>
    </div>
    <div class="kids-warning">
      <svg viewBox="0 0 50 48" fill="none" stroke="#fff" stroke-width="2.5"><polygon points="15,2 35,2 48,14 48,34 35,46 15,46 2,34 2,14"/><path d="M20 7 H30 M20 41 H30"/></svg>
      <p class="kids-warning__text">NOT SAFE<br>FOR KIDS</p>
    </div>
  </section>

  <section class="label label--coffee">
    <h1 class="brand">fizz</h1><span class="brand__tm">TM</span>
    <p class="tagline">infused ice cubes</p>
    <div class="cubes-art" role="img" aria-label="Line illustration of three stacked melting ice cubes in coffee brown"></div>
    <div class="tray">
      <div class="tray__bar">5mg per cube</div>
      <svg class="tray__wells" viewBox="0 0 171 26" fill="none" stroke="currentColor" stroke-width="2" style="color:var(--ink)">
        <path d="M6 1 L10 25 H29 L32 1 M37 1 L40 25 H59 L62 1 M69 1 L72 25 H91 L94 1 M101 1 L104 25 H123 L126 1 M133 1 L136 25 H156 L160 1"/>
      </svg>
    </div>
    <h2 class="flavour">coffee</h2>
    <p class="dose">50mg per tray</p>
    <div class="thc-warning">
      <svg width="42" height="36" viewBox="0 0 42 36" fill="none" stroke="#fff" stroke-width="2.5" stroke-linejoin="round"><path d="M21 3 L39 33 H3 Z"/></svg>
      <span class="thc-warning__text">CONTAINS THC</span>
    </div>
    <div class="kids-warning">
      <svg viewBox="0 0 50 48" fill="none" stroke="#fff" stroke-width="2.5"><polygon points="15,2 35,2 48,14 48,34 35,46 15,46 2,34 2,14"/><path d="M20 7 H30 M20 41 H30"/></svg>
      <p class="kids-warning__text">NOT SAFE<br>FOR KIDS</p>
    </div>
  </section>

  <section class="label label--classic">
    <h1 class="brand">fizz</h1><span class="brand__tm">TM</span>
    <p class="tagline">infused ice cubes</p>
    <div class="cubes-art" role="img" aria-label="Line illustration of three stacked melting ice cubes in white"></div>
    <div class="tray">
      <div class="tray__bar">5mg per cube</div>
      <svg class="tray__wells" viewBox="0 0 171 26" fill="none" stroke="currentColor" stroke-width="2" style="color:var(--ink)">
        <path d="M6 1 L10 25 H29 L32 1 M37 1 L40 25 H59 L62 1 M69 1 L72 25 H91 L94 1 M101 1 L104 25 H123 L126 1 M133 1 L136 25 H156 L160 1"/>
      </svg>
    </div>
    <h2 class="flavour">classic</h2>
    <p class="dose">50mg per tray</p>
    <div class="thc-warning">
      <svg width="42" height="36" viewBox="0 0 42 36" fill="none" stroke="#fff" stroke-width="2.5" stroke-linejoin="round"><path d="M21 3 L39 33 H3 Z"/></svg>
      <span class="thc-warning__text">CONTAINS THC</span>
    </div>
    <div class="kids-warning">
      <svg viewBox="0 0 50 48" fill="none" stroke="#fff" stroke-width="2.5"><polygon points="15,2 35,2 48,14 48,34 35,46 15,46 2,34 2,14"/><path d="M20 7 H30 M20 41 H30"/></svg>
      <p class="kids-warning__text">NOT SAFE<br>FOR KIDS</p>
    </div>
  </section>

</main>
</body>
</html>
```